Business card with professional look

I would like a creative yet professional looking business card for our business. We sell broadcast TV related security products for mobile phones, set top boxes, and tablets. Our customers are international. We have a logo we like and I would like to possibly add some color to the business card but keep it professional looking.

Target Market(s)

Professionals in the TV, cable, ans Satellite industries

Industry/Entity Type

Cable Tv

Contact Information for Business Card

Name Ned Vastermill, title CEO, Address 8130 Harborline Court, Suite 400, Del Arvo, CA 91584 USA, phone numbers m:+1.619.284.7302 o:+1.855.672.9140, email, logo

Font styles to use
Other font styles liked:
• Open to any font that looks good with logo

Requirements
Must have
• professional look with colors coordinated with logo colors. would like to add one or two different colors as well as some form of background color

```html
<!DOCTYPE html>
<html lang="en">
<head>
<meta charset="utf-8">
<title>Vantlock — Business Card</title>
<link rel="stylesheet" href="https://fonts.googleapis.com/css2?family=Lato:wght@400;700;900&display=swap">
<style>
  :root {
    --backdrop: #3b3b3b;
    --paper: #ffffff;
    --divider: #8a8f96;
    --blue-light: #2596d6;
    --blue-deep: #0b5aa6;
    --ink-dark: #4a4a4c;
    --ink-light: #ffffff;
  }
  * { box-sizing: border-box; margin: 0; padding: 0; }
  html, body {
    width: 1200px; height: 810px; overflow: hidden;
    background: var(--backdrop);
    font-family: "Lato", Arial, sans-serif;
  }
  .business-card {
    position: absolute; left: 150px; top: 148px;
    width: 900px; height: 514px;
    display: flex;
    box-shadow: 0 14px 40px rgba(0,0,0,.45);
  }
  .card-front {
    width: 470px; height: 100%;
    background: var(--paper);
    display: flex; align-items: center; justify-content: center;
    gap: 16px;
  }
  .brand-mark {
    width: 34px; height: 34px;
    background: var(--blue-deep);
    border-radius: 6px;
  }
  .brand-name {
    font-weight: 900;
    font-size: 58px;
    letter-spacing: -1px;
    color: var(--ink-dark);
  }
  .card-divider { width: 4px; background: var(--divider); }
  .card-back {
    flex: 1; height: 100%;
    background: linear-gradient(135deg, var(--blue-light) 0%, #1a7cc4 45%, var(--blue-deep) 100%);
    color: var(--ink-light);
    padding: 92px 40px 0 60px;
  }
  .holder-name { font-size: 32px; font-weight: 700; line-height: 1.1; white-space: nowrap; }
  .holder-title { font-size: 21px; margin: 2px 0 0 18px; }
  .address {
    font-size: 19px; line-height: 1.35;
    margin: 34px 0 0 44px;
  }
  .address span { display: block; white-space: nowrap; }
  .address span:nth-child(2) { padding-left: 14px; }
  .address span:nth-child(3) { padding-left: 28px; }
  .contact-list {
    list-style: none;
    font-size: 19px; line-height: 1.35;
    margin: 34px 0 0 90px;
  }
  .contact-list li { display: flex; align-items: center; gap: 6px; white-space: nowrap; }
  .contact-list li:nth-child(2) { padding-left: 14px; }
  .contact-list li:nth-child(3) { padding-left: 28px; }
  .contact-icon { width: 15px; height: 15px; fill: var(--ink-light); flex: none; }
</style>
</head>
<body>
  <div class="business-card">
    <section class="card-front">
      <span class="brand-mark"></span>
      <span class="brand-name">Vantlock</span>
    </section>
    <div class="card-divider"></div>
    <section class="card-back">
      <h1 class="holder-name">Ned Vastermill</h1>
      <p class="holder-title">CEO</p>
      <p class="address">
        <span>8130 Harborline Court</span>
        <span>Suite 400</span>
        <span>Del Arvo, CA 91584 USA</span>
      </p>
      <ul class="contact-list">
        <li>
          <svg class="contact-icon" viewBox="0 0 16 16" aria-hidden="true"><path d="M3.2 1.5 5.6 4c.4.4.4 1 0 1.4L4.5 6.5a9 9 0 0 0 5 5l1.1-1.1c.4-.4 1-.4 1.4 0l2.5 2.4c.4.4.4 1 0 1.4l-1.2 1.2C11 16.6 0 5.6 1.6 3.1l1.2-1.2c.1-.2.3-.4.4-.4z"/></svg>
          +1.619.284.7302
        </li>
        <li>
          <svg class="contact-icon" viewBox="0 0 16 16" aria-hidden="true"><path d="M4 0h8a1 1 0 0 1 1 1v14a1 1 0 0 1-1 1H4a1 1 0 0 1-1-1V1a1 1 0 0 1 1-1zm.5 2v10.5h7V2zM8 13.3a.9.9 0 1 0 0 1.8.9.9 0 0 0 0-1.8z"/></svg>
          +1.855.672.9140
        </li>
        <li>
          <svg class="contact-icon" viewBox="0 0 16 16" aria-hidden="true"><path d="M1 3h14v10H1zm1.2 1.2L8 8.6l5.8-4.4zM2 5.4V12h12V5.4L8 10z"/></svg>
          info@vantlock.com
        </li>
      </ul>
    </section>
  </div>
</body>
</html>
```